Visitenkarten-Design für Gesundheits- und Ernährungsberaterin
Zielgruppe
Ich bin Gesundheit und Ernährungsberaterin
Zielgruppe sind chronisch Kranke und Gesundheitsbewusste Personen
Aufgabenstellung
Schlichtes aber direkt erkennbares Design.
Mahl mit Maß , Gesundheit und Ernährungsberatung ( gut lesbar , elegant)
Marlene Obruk-Feistinger ( nicht so groß )
Grau ; Grün Töne und gerne etwas rosa
Infos wie Adresse und E-Mail vielleicht in jeweilige Blöcke am unteren Rand

```html
<!DOCTYPE html>
<html lang="de">
<head>
<meta charset="utf-8">
<title>Visitenkarten – Mahl mit Maß</title>
<link rel="stylesheet" href="https://fonts.googleapis.com/css2?family=Questrial&family=Montserrat:wght@700&display=swap">
<style>
  :root {
    --green: #8fd45e;
    --green-light: #c5e8b0;
    --grey: #656565;
    --pink: #dc8886;
    --text: #555555;
    --paper: #ffffff;
  }
  * { margin: 0; padding: 0; box-sizing: border-box; }
  html, body { width: 861px; height: 1200px; overflow: hidden; background: var(--paper); }
  body { position: relative; font-family: "Questrial", sans-serif; color: var(--text); }

  .card {
    position: absolute;
    width: 336px; height: 220px;
    background: var(--paper);
    box-shadow: 4px 5px 8px rgba(0,0,0,0.28);
    overflow: hidden;
  }
  .card--left { left: 67px; }
  .card--right { left: 438px; }
  .row-1 { top: 47px; }
  .row-2 { top: 331px; }
  .row-3 { top: 615px; }
  .row-4 { top: 909px; }

  .scheme-green { --outer: var(--green); --inner: var(--green-light); }
  .scheme-grey  { --outer: var(--green); --inner: var(--grey); }
  .scheme-rose  { --outer: var(--pink);  --inner: var(--green-light); }
  .scheme-mixed { --outer: var(--green); --inner: var(--pink); }

  .bands { position: absolute; inset: 0; width: 336px; height: 220px; }
  .band-outer { fill: var(--outer); }
  .band-inner { fill: var(--inner); }

  .brand {
    position: absolute;
    display: flex; align-items: center; gap: 6px;
    color: var(--green);
    white-space: nowrap;
  }
  .brand-dot { border-radius: 50%; background: var(--green); flex: none; }
  .card--left .brand { left: 0; right: 0; top: 92px; justify-content: center; font-size: 24px; }
  .card--left .brand-dot { width: 16px; height: 16px; }
  .card--right .brand { right: 10px; top: 48px; font-size: 15px; }
  .card--right .brand-dot { width: 10px; height: 10px; }

  .tagline {
    position: absolute;
    color: var(--pink);
    text-transform: uppercase;
    letter-spacing: 0.09em;
    white-space: nowrap;
  }
  .card--left .tagline { left: 0; right: 0; top: 165px; text-align: center; font-size: 13.5px; }
  .card--right .tagline { right: 8px; top: 103px; font-size: 9.5px; }

  .person { position: absolute; left: 18px; top: 124px; }
  .person-name {
    font-family: "Montserrat", sans-serif; font-weight: 700;
    font-size: 10px; text-transform: uppercase; color: var(--grey); letter-spacing: 0.01em;
  }
  .person-role { font-size: 6.6px; text-transform: uppercase; margin-top: 1px; }

  .address, .contact {
    position: absolute; top: 163px;
    font-size: 8.2px; line-height: 10.5px; text-transform: uppercase; white-space: nowrap;
  }
  .address { left: 18px; }
  .contact { left: 164px; display: grid; grid-template-columns: 33px auto; }
</style>
</head>
<body>

<!-- Row 1 -->
<section class="card card--left row-1 scheme-green">
  <svg class="bands" viewBox="0 0 336 220" aria-hidden="true">
    <path class="band-outer" d="M0,0 H300 C200,9 90,12 0,12 Z"/>
    <path class="band-inner" d="M0,15 C120,15 250,8 336,0 C240,14 110,30 0,30 Z"/>
    <path class="band-inner" d="M0,190 C120,190 250,205 336,220 C240,212 110,204 0,205 Z"/>
    <path class="band-outer" d="M0,208 C90,208 200,212 300,220 H0 Z"/>
  </svg>
  <div class="brand"><span class="brand-dot"></span>Mahl mit Maß</div>
  <p class="tagline">Mahl mit Maß.</p>
</section>
<section class="card card--right row-1 scheme-green">
  <svg class="bands" viewBox="0 0 336 220" aria-hidden="true">
    <path class="band-outer" d="M0,0 H300 C200,9 90,12 0,12 Z"/>
    <path class="band-inner" d="M0,15 C120,15 250,8 336,0 C240,14 110,30 0,30 Z"/>
    <path class="band-inner" d="M0,190 C120,190 250,205 336,220 C240,212 110,204 0,205 Z"/>
    <path class="band-outer" d="M0,208 C90,208 200,212 300,220 H0 Z"/>
  </svg>
  <div class="brand"><span class="brand-dot"></span>Mahl mit Maß</div>
  <p class="tagline">Mahl mit Maß.</p>
  <div class="person"><p class="person-name">Marlene Obruk-Feistinger</p><p class="person-role">Gesundheits- und Ernährungsberaterin</p></div>
  <p class="address">Lindenweg 7<br>31582 Weidenfeld</p>
  <p class="contact"><span>Tel</span><span>05123 / 482 71 06</span><span>Mobil</span><span>0160 / 73 25 18 40</span><span>Mail</span><span>beratung-mof@postfach.de</span></p>
</section>

<!-- Row 2 -->
<section class="card card--left row-2 scheme-grey">
  <svg class="bands" viewBox="0 0 336 220" aria-hidden="true">
    <path class="band-outer" d="M0,0 H300 C200,9 90,12 0,12 Z"/>
    <path class="band-inner" d="M0,15 C120,15 250,8 336,0 C240,14 110,30 0,30 Z"/>
    <path class="band-inner" d="M0,190 C120,190 250,205 336,220 C240,212 110,204 0,205 Z"/>
    <path class="band-outer" d="M0,208 C90,208 200,212 300,220 H0 Z"/>
  </svg>
  <div class="brand"><span class="brand-dot"></span>Mahl mit Maß</div>
  <p class="tagline">Mahl mit Maß.</p>
</section>
<section class="card card--right row-2 scheme-grey">
  <svg class="bands" viewBox="0 0 336 220" aria-hidden="true">
    <path class="band-outer" d="M0,0 H300 C200,9 90,12 0,12 Z"/>
    <path class="band-inner" d="M0,15 C120,15 250,8 336,0 C240,14 110,30 0,30 Z"/>
    <path class="band-inner" d="M0,190 C120,190 250,205 336,220 C240,212 110,204 0,205 Z"/>
    <path class="band-outer" d="M0,208 C90,208 200,212 300,220 H0 Z"/>
  </svg>
  <div class="brand"><span class="brand-dot"></span>Mahl mit Maß</div>
  <p class="tagline">Mahl mit Maß.</p>
  <div class="person"><p class="person-name">Marlene Obruk-Feistinger</p><p class="person-role">Gesundheits- und Ernährungsberaterin</p></div>
  <p class="address">Lindenweg 7<br>31582 Weidenfeld</p>
  <p class="contact"><span>Tel</span><span>05123 / 482 71 06</span><span>Mobil</span><span>0160 / 73 25 18 40</span><span>Mail</span><span>beratung-mof@postfach.de</span></p>
</section>

<!-- Row 3 -->
<section class="card card--left row-3 scheme-rose">
  <svg class="bands" viewBox="0 0 336 220" aria-hidden="true">
    <path class="band-outer" d="M0,0 H300 C200,9 90,12 0,12 Z"/>
    <path class="band-inner" d="M0,15 C120,15 250,8 336,0 C240,14 110,30 0,30 Z"/>
    <path class="band-inner" d="M0,190 C120,190 250,205 336,220 C240,212 110,204 0,205 Z"/>
    <path class="band-outer" d="M0,208 C90,208 200,212 300,220 H0 Z"/>
  </svg>
  <div class="brand"><span class="brand-dot"></span>Mahl mit Maß</div>
  <p class="tagline">Mahl mit Maß.</p>
</section>
<section class="card card--right row-3 scheme-rose">
  <svg class="bands" viewBox="0 0 336 220" aria-hidden="true">
    <path class="band-outer" d="M0,0 H300 C200,9 90,12 0,12 Z"/>
    <path class="band-inner" d="M0,15 C120,15 250,8 336,0 C240,14 110,30 0,30 Z"/>
    <path class="band-inner" d="M0,190 C120,190 250,205 336,220 C240,212 110,204 0,205 Z"/>
    <path class="band-outer" d="M0,208 C90,208 200,212 300,220 H0 Z"/>
  </svg>
  <div class="brand"><span class="brand-dot"></span>Mahl mit Maß</div>
  <p class="tagline">Mahl mit Maß.</p>
  <div class="person"><p class="person-name">Marlene Obruk-Feistinger</p><p class="person-role">Gesundheits- und Ernährungsberaterin</p></div>
  <p class="address">Lindenweg 7<br>31582 Weidenfeld</p>
  <p class="contact"><span>Tel</span><span>05123 / 482 71 06</span><span>Mobil</span><span>0160 / 73 25 18 40</span><span>Mail</span><span>beratung-mof@postfach.de</span></p>
</section>

<!-- Row 4 -->
<section class="card card--left row-4 scheme-mixed">
  <svg class="bands" viewBox="0 0 336 220" aria-hidden="true">
    <path class="band-outer" d="M0,0 H300 C200,9 90,12 0,12 Z"/>
    <path class="band-inner" d="M0,15 C120,15 250,8 336,0 C240,14 110,30 0,30 Z"/>
    <path class="band-inner" d="M0,190 C120,190 250,205 336,220 C240,212 110,204 0,205 Z"/>
    <path class="band-outer" d="M0,208 C90,208 200,212 300,220 H0 Z"/>
  </svg>
  <div class="brand"><span class="brand-dot"></span>Mahl mit Maß</div>
  <p class="tagline">Mahl mit Maß.</p>
</section>
<section class="card card--right row-4 scheme-mixed">
  <svg class="bands" viewBox="0 0 336 220" aria-hidden="true">
    <path class="band-outer" d="M0,0 H300 C200,9 90,12 0,12 Z"/>
    <path class="band-inner" d="M0,15 C120,15 250,8 336,0 C240,14 110,30 0,30 Z"/>
    <path class="band-inner" d="M0,190 C120,190 250,205 336,220 C240,212 110,204 0,205 Z"/>
    <path class="band-outer" d="M0,208 C90,208 200,212 300,220 H0 Z"/>
  </svg>
  <div class="brand"><span class="brand-dot"></span>Mahl mit Maß</div>
  <p class="tagline">Mahl mit Maß.</p>
  <div class="person"><p class="person-name">Marlene Obruk-Feistinger</p><p class="person-role">Gesundheits- und Ernährungsberaterin</p></div>
  <p class="address">Lindenweg 7<br>31582 Weidenfeld</p>
  <p class="contact"><span>Tel</span><span>05123 / 482 71 06</span><span>Mobil</span><span>0160 / 73 25 18 40</span><span>Mail</span><span>beratung-mof@postfach.de</span></p>
</section>

</body>
</html>
```